Lone Prairie Canvas & Sound Jubilee

Organization:
Lone Prairie Canvas and Sound Jubilee is a non-profit organization created by a group of anonymous donors to bring more fun, culture, and art to a small Texas town. Our mission is to promote art and music in Washington County.
The multi-day eclectic festival will feature three stages, a film, art vendors, live mural artists, and food trucks set up throughout historic downtown Brenham. The event is FREE to the public.
Goals:
We need an attractive poster to publicize the festival.
Details:
Lone Prairie Canvas and Sound Jubilee
Friday, October 14 – 16
Free admission (VIP tickets available)
Live music- 3 stages/10 bands
Film Screening
Art vendors and art walk
Live art murals
Food trucks
www.loneprairiecanvasandsoundjubilee.example
#loneprairiecanvasandsound
Requirements:
Please incorporate our festival logo attached.
Conclusion:
After selecting a poster design, we hope to continue to work with the artist to design other event materials including website splash page and rack cards using design elements from the poster.

```html
<!DOCTYPE html>
<html lang="en">
<head>
<meta charset="utf-8">
<title>Lone Prairie Canvas &amp; Sound Jubilee</title>
<link rel="stylesheet" href="https://fonts.googleapis.com/css2?family=Montserrat:wght@400;500;600;700&display=swap">
<style>
  :root {
    --ink: #ffffff;
    --night: #120a12;
    --plum: #2a1424;
    --title-glow: rgba(170, 40, 60, 0.9);
    --badge: #6a3a1c;
    --seam: #140a10;
  }
  * { margin: 0; padding: 0; box-sizing: border-box; }
  html, body { width: 776px; height: 1200px; overflow: hidden; background: var(--night); }
  .poster {
    position: relative;
    width: 776px;
    height: 1200px;
    overflow: hidden;
    background: radial-gradient(ellipse at 50% 45%, var(--plum) 0%, var(--night) 80%);
    font-family: "Montserrat", sans-serif;
    color: var(--ink);
  }
  .collage { position: absolute; inset: 0; width: 776px; height: 1200px; }
  .line {
    position: absolute;
    left: 0; right: 0;
    text-align: center;
    white-space: nowrap;
  }
  .festival-name {
    top: 843px; line-height: 38px;
    font-size: 26px; font-weight: 600;
    letter-spacing: 5.6px;
    text-shadow: 2px 2px 0 var(--title-glow);
  }
  .admission { top: 891px; line-height: 40px; font-size: 30px; font-weight: 400; }
  .dates { top: 941px; line-height: 50px; font-size: 40px; font-weight: 700; }
  .feature { line-height: 32px; font-size: 24px; font-weight: 400; }
  .feature-music { top: 1003px; }
  .feature-art { top: 1044px; }
  .feature-food { top: 1085px; }
  .website { top: 1134px; line-height: 28px; font-size: 21px; font-weight: 400; }
  .organiser-mark {
    position: absolute;
    right: 12px; bottom: 30px;
    display: flex; align-items: center; gap: 6px;
  }
  .organiser-mark span {
    font-size: 8px; font-weight: 500; line-height: 10px; text-align: right;
  }
  .organiser-mark i {
    display: block; width: 52px; height: 68px; background: var(--badge);
  }
</style>
</head>
<body>
<main class="poster">
  <svg class="collage" viewBox="0 0 776 1200">
    <defs>
      <linearGradient id="duo-tone" x1="0" y1="0" x2="1" y2="1">
        <stop offset="0" stop-color="#4a3a32"/><stop offset="0.5" stop-color="#6a5244"/><stop offset="1" stop-color="#2a1a1e"/>
      </linearGradient>
      <linearGradient id="smile-tone" x1="0" y1="0" x2="1" y2="1">
        <stop offset="0" stop-color="#8a6a4a"/><stop offset="0.45" stop-color="#d2ae8a"/><stop offset="1" stop-color="#6a4a36"/>
      </linearGradient>
      <linearGradient id="guitar-tone" x1="0" y1="0" x2="1" y2="1">
        <stop offset="0" stop-color="#3a1016"/><stop offset="0.5" stop-color="#a83024"/><stop offset="1" stop-color="#5a1a1c"/>
      </linearGradient>
      <linearGradient id="stage-tone" x1="0" y1="0" x2="1" y2="1">
        <stop offset="0" stop-color="#4a5a7a"/><stop offset="0.5" stop-color="#c0362c"/><stop offset="1" stop-color="#3a2630"/>
      </linearGradient>
      <linearGradient id="portrait-tone" x1="0" y1="0" x2="0" y2="1">
        <stop offset="0" stop-color="#5a3e36"/><stop offset="0.5" stop-color="#3a2428"/><stop offset="1" stop-color="#1a0e14" stop-opacity="0"/>
      </linearGradient>
      <linearGradient id="band-tone" x1="0" y1="0" x2="0" y2="1">
        <stop offset="0" stop-color="#4a2a2e"/><stop offset="0.5" stop-color="#5e4036"/><stop offset="1" stop-color="#1a0e14" stop-opacity="0"/>
      </linearGradient>
      <radialGradient id="vignette" cx="0.5" cy="0.35" r="0.75">
        <stop offset="0.55" stop-color="#120a12" stop-opacity="0"/><stop offset="1" stop-color="#120a12" stop-opacity="0.7"/>
      </radialGradient>
    </defs>
    <rect width="776" height="880" fill="#1e1016"/>
    <polygon points="90,0 720,0 600,230 395,350 250,300 200,60" fill="url(#duo-tone)" role="img" aria-label="Portrait of a man in sunglasses beside a dark-haired woman"/>
    <polygon points="0,100 200,60 375,360 190,540 0,520" fill="url(#smile-tone)" role="img" aria-label="Portrait of a smiling young singer with long hair"/>
    <polygon points="720,40 776,60 776,515 580,560 405,350 600,230" fill="url(#guitar-tone)" role="img" aria-label="Guitarist in a vest singing upward under red light"/>
    <polygon points="190,540 375,360 580,560 455,695 300,720" fill="url(#stage-tone)" role="img" aria-label="Singer in a red suit performing on stage with a band"/>
    <polygon points="0,540 190,545 300,720 430,870 0,870" fill="url(#portrait-tone)" role="img" aria-label="Portrait of a long-haired bearded musician"/>
    <polygon points="455,695 580,560 776,515 776,880 500,880" fill="url(#band-tone)" role="img" aria-label="Band members seated in a row"/>
    <g stroke="var(--seam)" stroke-width="5" fill="none">
      <polyline points="200,60 375,360 580,560 776,515"/>
      <polyline points="375,360 600,230 720,40"/>
      <polyline points="0,520 190,540 300,720"/>
      <polyline points="190,540 375,360"/>
      <polyline points="455,695 580,560"/>
    </g>
    <rect width="776" height="1200" fill="url(#vignette)"/>
  </svg>

  <h1 class="line festival-name">Lone Prairie Canvas &amp; Sound Jubilee</h1>
  <p class="line admission">Free admission (VIP tickets available)</p>
  <p class="line dates">Friday, October 14 – 16</p>
  <p class="line feature feature-music">Live music- 3 stages/10 bands / Film Screening</p>
  <p class="line feature feature-art">Art vendors and art walk /Live art murals</p>
  <p class="line feature feature-food">Food trucks</p>
  <p class="line website">www.loneprairiecanvasandsoundjubilee.example</p>

  <div class="organiser-mark">
    <span>Lone Prairie<br>Canvas &amp; Sound<br>Jubilee</span>
    <i></i>
  </div>
</main>
</body>
</html>
```